Banner
Zielgruppe
Wir sind Estrichleger und Beschichter. Wir erstellen u. a. Sichtestrich und Beschichtungen im Wohnbereich und für Gewerbekunden im Industriebereich (Hallen und Tiefgaragen).
Unsere Zielgruppe sind sowohl Privatverbraucher im gehobenen Segment als auch Bauträger und Gewerbekunden
Aufgabenstellung
Gute Lesbarkeit, klare Botschaft auch wenn die Banner in großer Höhe angebracht werden.
Masse:
Bauzaunbanner aus Mesh-Plane, 340x173 cm,
wird gedruckt auf
hochwertige Mehs-Plane, rundum, umsäumt und veröst, 4/0-farbig (einseitig mit Motiv bedruck), 270 g Meshgewebe-Plane - winddurchlässig und wetterfest, (B1- zertifiziert - schwer entflammbar nach DIN 4102)
Es ist wünschenswert den Claim: 'Ich steh drauf' mit auf dem Banner zu platzieren.
Wir haben gerade die Fahrzeuge neu designen lassen, der Gewinner ist hochgeladen. Gern können Sie sich an diesem orientieren.

```html
<!DOCTYPE html>
<html lang="de">
<head>
<meta charset="utf-8">
<title>KB Estrichbau – Bauzaunbanner</title>
<link href="https://fonts.googleapis.com/css2?family=Open+Sans:wght@400;500&display=swap" rel="stylesheet">
<style>
  :root {
    --ink: #000000;
    --red: #b3262d;
    --white: #ffffff;
    --concrete-light: #c9c9c7;
    --concrete-mid: #a4a4a2;
  }
  html, body {
    margin: 0;
    padding: 0;
    width: 1200px;
    height: 611px;
    overflow: hidden;
    background: var(--ink);
    font-family: "Open Sans", sans-serif;
  }
  .banner {
    position: relative;
    width: 1200px;
    height: 611px;
    background: var(--ink);
  }
  .headline {
    position: absolute;
    top: 2px;
    left: 0;
    width: 100%;
    margin: 0;
    text-align: center;
    color: var(--red);
    font-weight: 400;
    font-size: 55px;
    line-height: 60px;
    letter-spacing: -0.5px;
  }
  .claim-text {
    position: absolute;
    top: 62px;
    left: 0;
    width: 100%;
    margin: 0;
    text-align: center;
    color: var(--white);
    font-size: 19.6px;
    line-height: 25px;
  }
  .gallery-tile {
    position: absolute;
    top: 122px;
    height: 367px;
  }
  .tile-shop {
    left: 0;
    width: 398px;
    background: linear-gradient(180deg, #d9d6d2 0%, #8d8f92 45%, #b9b9b8 70%, #a9a9a8 100%);
  }
  .tile-hearth {
    left: 408px;
    width: 446px;
    background: linear-gradient(160deg, #b9b6b1 0%, var(--concrete-light) 45%, #bcae9a 75%, var(--concrete-mid) 100%);
  }
  .tile-stair {
    left: 864px;
    width: 336px;
    background: linear-gradient(200deg, #d6d2cc 0%, #4a4a4a 35%, var(--concrete-mid) 60%, var(--concrete-light) 100%);
  }
  .brand {
    position: absolute;
    top: 524px;
    width: 268px;
    height: 40px;
    display: flex;
    align-items: center;
    gap: 10px;
  }
  .brand-left { left: 23px; }
  .brand-right { left: 906px; }
  .brand-square {
    flex: none;
    width: 16px;
    height: 16px;
    background: var(--red);
  }
  .brand-name {
    margin: 0;
    color: var(--red);
    font-size: 24px;
    font-weight: 500;
    letter-spacing: 2px;
    white-space: nowrap;
    line-height: 40px;
  }
  .contact {
    position: absolute;
    top: 495px;
    margin: 0;
    color: var(--white);
    font-size: 28.5px;
    line-height: 34.5px;
    font-style: normal;
    white-space: nowrap;
  }
  .contact-address { left: 309px; }
  .contact-channels { left: 544px; }
  .contact span { display: block; }
</style>
</head>
<body>
  <main class="banner">
    <h1 class="headline">„ICH STEH DRAUF“</h1>
    <p class="claim-text">Höchste Qualität spiegelt sich in der sauber durchdachten Planung, der umsichtigen Auswahl der Materialien, der handwerklich<br>meisterlichen Durchführung und nicht zuletzt im ausgezeichneten Preis-Leistungsverhältnis.</p>

    <div class="gallery-tile tile-shop" role="img" aria-label="Ladengeschäft mit glänzendem grauem Sichtestrichboden"></div>
    <div class="gallery-tile tile-hearth" role="img" aria-label="Wohnraum mit Betonkamin, Sichtestrich-Podest und Holzstufen"></div>
    <div class="gallery-tile tile-stair" role="img" aria-label="Treppenabgang mit wolkig grauem Sichtestrichboden"></div>

    <div class="brand brand-left">
      <span class="brand-square"></span>
      <p class="brand-name">KB ESTRICHBAU</p>
    </div>

    <address class="contact contact-address">
      <span>Konrad Brenntal</span>
      <span>Lindenweg 7b</span>
      <span>83999 Almhofen</span>
    </address>
    <address class="contact contact-channels">
      <span>(0 12 34) 56 78 90 1</span>
      <span>info@kb-estrichbau.de</span>
      <span>www.kb-estrichbau.de</span>
    </address>

    <div class="brand brand-right">
      <span class="brand-square"></span>
      <p class="brand-name">KB ESTRICHBAU</p>
    </div>
  </main>
</body>
</html>
```